We need a refreshed business card. Our company is a venture capital investment firm focused on investing in medical devices. Logo is attached. please also see our website www.velmoracapital.example

Target Market(s)

investors and potential investment targets

Industry/Entity Type

medical investments

Contact Information for Business Card

logo, name, title, email, phone, website, address,

Colors
0054AA
0677BA
7BADD7
CADEEF
E8F1F8
0094D4
00A9DD
6FCCEA
C7EBF8
E9F6FB
00AB8E
00BBA5
67D7C9
C6EFE9
E9F9F6

Requirements
Must have
• fresh modern design
Nice to have
• QR code leading to our linked in page, short description of what we do “Early Stage Medical Device Investors”

```html
<!DOCTYPE html>
<html lang="en">
<head>
<meta charset="utf-8">
<title>Velmora Capital Partners – Business Card</title>
<link href="https://fonts.googleapis.com/css2?family=Montserrat:wght@400;500;600;700&display=swap" rel="stylesheet">
<style>
  :root {
    --brand-blue: #0d55a6;
    --brand-teal: #19a58c;
    --ink: #2b2b2b;
    --muted: #5a5a5a;
    --rule: #c9c9c9;
    --paper: #ffffff;
    --backdrop: #ebebeb;
  }
  * { box-sizing: border-box; margin: 0; padding: 0; }
  html, body { width: 1200px; height: 1164px; overflow: hidden; }
  body {
    background: var(--backdrop);
    font-family: "Montserrat", sans-serif;
    position: relative;
  }
  .card {
    position: absolute;
    left: 160px;
    width: 880px;
    height: 527px;
    overflow: hidden;
    box-shadow: 0 2px 8px rgba(0,0,0,0.12);
  }
  .card--front { top: 36px; background: var(--paper); }
  .card--back { top: 600px; background: var(--brand-blue); }

  /* Front */
  .front-logo {
    position: absolute;
    left: 110px;
    top: 185px;
    width: 320px;
    text-align: center;
  }
  .wordmark {
    font-weight: 700;
    font-size: 62px;
    line-height: 1;
    letter-spacing: -0.5px;
    color: var(--brand-blue);
    white-space: nowrap;
  }
  .front-logo .tagline {
    margin-top: 18px;
    font-size: 17px;
    font-weight: 500;
    color: var(--muted);
    letter-spacing: 0.2px;
    text-transform: uppercase;
    white-space: nowrap;
  }
  .divider {
    position: absolute;
    width: 2px;
    background: var(--rule);
  }
  .card--front .divider { left: 446px; top: 146px; height: 218px; }
  .contact {
    position: absolute;
    left: 467px;
    top: 144px;
  }
  .contact .name {
    font-size: 28px;
    font-weight: 600;
    color: var(--brand-blue);
  }
  .contact .title {
    margin-top: 4px;
    font-size: 19px;
    color: var(--brand-teal);
  }
  .contact ul { list-style: none; margin-top: 20px; }
  .contact li {
    display: flex;
    align-items: center;
    gap: 14px;
    font-size: 20px;
    color: var(--ink);
    height: 33px;
    white-space: nowrap;
  }
  .contact li svg { width: 20px; height: 20px; flex: none; }
  .band {
    position: absolute;
    left: 0;
    bottom: 0;
    width: 880px;
    height: 24px;
  }

  /* Back */
  .back-logo {
    position: absolute;
    right: 405px;
    top: 222px;
    text-align: right;
  }
  .back-logo .wordmark { color: var(--paper); font-size: 62px; }
  .card--back .divider { left: 497px; top: 174px; height: 162px; background: #ffffff; opacity: 0.85; }
  .back-tagline {
    position: absolute;
    left: 520px;
    top: 222px;
    color: var(--paper);
    font-size: 20px;
    line-height: 29px;
    text-transform: uppercase;
    letter-spacing: 0.3px;
  }
</style>
</head>
<body>

  <section class="card card--front" aria-label="Card front">
    <div class="front-logo">
      <div class="wordmark">Velmora</div>
      <div class="tagline">Velmora Capital Partners</div>
    </div>
    <div class="divider"></div>
    <div class="contact">
      <div class="name">Daniel Reyes</div>
      <div class="title">President</div>
      <ul>
        <li>
          <svg viewBox="0 0 20 20" aria-hidden="true"><path d="M5 2.5l3 3-1.6 2a10 10 0 0 0 6.1 6.1l2-1.6 3 3-2 2.3C9 17 3 11 2.7 4.5z" fill="var(--brand-teal)"/><path d="M12 3.5a5 5 0 0 1 4.5 4.5M12 6.5a2.2 2.2 0 0 1 1.8 1.8" stroke="var(--brand-teal)" stroke-width="1.4" fill="none"/></svg>
          555 0142 387
        </li>
        <li>
          <svg viewBox="0 0 20 20" aria-hidden="true"><rect x="2" y="5" width="16" height="11" fill="var(--brand-teal)"/><path d="M2 5l8 6 8-6M2 16l6-5M18 16l-6-5" stroke="#fff" stroke-width="1.3" fill="none"/></svg>
          daniel@velmoracapital.example
        </li>
        <li>
          <svg viewBox="0 0 20 20" aria-hidden="true"><circle cx="10" cy="10" r="7.5" fill="none" stroke="var(--brand-teal)" stroke-width="1.6"/><ellipse cx="10" cy="10" rx="3.2" ry="7.5" fill="none" stroke="var(--brand-teal)" stroke-width="1.4"/><path d="M2.5 10h15M4 6h12M4 14h12" stroke="var(--brand-teal)" stroke-width="1.3"/></svg>
          www.velmoracapital.example
        </li>
        <li>
          <svg viewBox="0 0 20 20" aria-hidden="true"><path d="M10 1.5a6 6 0 0 0-6 6c0 4.5 6 11 6 11s6-6.5 6-11a6 6 0 0 0-6-6z" fill="var(--brand-teal)"/><circle cx="10" cy="7.5" r="2.2" fill="#fff"/></svg>
          210 Harbor Lane, Suite 4
        </li>
      </ul>
    </div>
    <svg class="band" viewBox="0 0 880 24" preserveAspectRatio="none" aria-hidden="true">
      <polygon points="0,0 439,0 432,24 0,24" fill="var(--brand-blue)"/>
      <polygon points="446,0 880,0 880,24 439,24" fill="var(--brand-teal)"/>
    </svg>
  </section>

  <section class="card card--back" aria-label="Card back">
    <div class="back-logo">
      <div class="wordmark">Velmora</div>
    </div>
    <div class="divider"></div>
    <div class="back-tagline">Velmora<br>Capital<br>Partners</div>
  </section>

</body>
</html>
```